Postcard for crestway homes

Create new 6.5 x 9 postcard for crestway homes.
FRONT: See attached postcard for the front, change Harbor Keystone logo with Crestway Homes logo. change Harbor Keystone above the phone # to Crestway Homes Myrtle Beach.
BACK: See attachment for text on the back. add postage and pictures to make it look professional.

```html
<!DOCTYPE html>
<html lang="en">
<head>
<meta charset="utf-8">
<title>Crestway Homes Postcard</title>
<link href="https://fonts.googleapis.com/css2?family=Outfit:wght@400;600;700;800;900&display=swap" rel="stylesheet">
<style>
:root{
  --navy:#17475a;
  --navy-deep:#133c4c;
  --teal:#1597c0;
  --teal-dark:#0f6f86;
  --ink:#1b2b33;
  --paper:#ffffff;
  --stage:#e9edef;
  --photo-a:#8a7460;
  --photo-b:#c9c1b6;
}
*{margin:0;padding:0;box-sizing:border-box}
html,body{width:1200px;height:600px;overflow:hidden;background:var(--stage);font-family:"Outfit",sans-serif;color:var(--ink)}
.side-label{position:absolute;top:60px;font-size:28px;font-weight:400;color:#111}
.side-label.front{left:242px}
.side-label.back{left:801px}
.card{position:absolute;top:118px;width:504px;height:364px;background:var(--paper);overflow:hidden;box-shadow:0 6px 18px rgba(0,0,0,.25)}
.card.front{left:75px}
.card.back{left:634px;background:linear-gradient(160deg,#fff 55%,#f2f4f5 75%,#fff 100%)}
.abs{position:absolute}

/* front */
.front-art{position:absolute;inset:0}
.brand-front{left:14px;top:40px;width:160px;text-align:center;color:var(--navy);font-weight:700;font-size:19px;line-height:1;white-space:nowrap}
.brand-front .dot{display:block;width:14px;height:14px;background:var(--teal);border-radius:50%;margin:0 auto 8px}
.brand-front small{display:block;font-size:7px;font-weight:600;letter-spacing:.5px;margin-top:6px}
.sell-box{left:23px;top:112px;width:131px;height:68px;border:2px solid var(--navy)}
.sell-word{left:23px;top:112px;width:131px;text-align:center;font-size:42px;font-weight:900;color:var(--navy);line-height:46px}
.home-band{left:23px;top:159px;width:131px;height:21px;background:var(--navy);color:#fff;font-size:16px;font-weight:800;text-align:center;line-height:21px}
.low-as{left:22px;top:181px;font-size:16px;font-weight:700;color:var(--teal);line-height:20px}
.pct{left:158px;top:150px;font-size:50px;font-weight:800;color:var(--teal);line-height:1}
.commission{left:21px;top:199px;font-size:32px;font-weight:900;color:var(--navy);letter-spacing:.3px;line-height:34px}
.note{left:24px;width:200px;padding-left:9px;border-left:2px solid var(--teal);color:#fff;font-size:9.4px;line-height:12px}
.note.one{top:265px}
.note.two{top:309px}
.cta-name{left:315px;top:283px;width:210px;font-size:12px;font-weight:600;color:var(--teal)}
.phone-pill{left:288px;top:303px;width:186px;height:24px;background:#fff;border-radius:12px;border:2px solid var(--navy);display:flex;align-items:center;gap:6px;padding-left:6px}
.phone-pill .num{font-size:21px;font-weight:800;color:var(--navy)}
.icon-circle{width:16px;height:16px;border-radius:50%;background:var(--navy);display:flex;align-items:center;justify-content:center}
.slogan{left:316px;top:333px;font-size:14.5px;font-weight:700;color:#fff}

/* back */
.save{left:26px;top:20px;font-size:19px;font-weight:800;color:var(--teal);letter-spacing:.3px;line-height:20px}
.fees-band{left:25px;top:40px;width:168px;height:20px;background:var(--navy);color:#fff;font-size:14px;font-weight:800;text-align:center;line-height:21px}
.local{left:25px;top:65px;font-size:8px;font-weight:700;line-height:10px}
.local b{color:var(--teal)}
.not-a{left:46px;top:82px;font-size:12px;font-weight:800;color:var(--navy);line-height:12px}
.discount{left:25px;top:93px;font-size:23px;font-weight:800;color:var(--teal-dark);line-height:22px}
.service-grid{left:25px;top:117px;width:234px;display:grid;grid-template-columns:repeat(3,1fr);grid-template-rows:32px 32px;gap:1px}
.service{border:1px solid #9fd3e3;background:#fff;font-size:6.4px;font-weight:600;line-height:8px;padding:0 8px;display:flex;align-items:center}
.whats{left:46px;top:192px;font-size:12px;font-weight:800;color:var(--teal);line-height:12px}
.worth{left:25px;top:203px;font-size:22px;font-weight:800;color:var(--navy);line-height:20px}
.email-band{left:25px;top:224px;width:235px;height:17px;background:var(--navy);color:#fff;font-size:13px;font-weight:800;text-align:center;line-height:18px}
.research{left:25px;top:244px;font-size:7.4px;font-weight:600;line-height:9px}
.send{left:25px;top:257px;font-size:7.4px;font-weight:600;line-height:9px}
.email-bar{left:25px;top:269px;width:139px;height:14px;background:var(--teal);color:#fff;font-size:7.2px;font-weight:600;display:flex;align-items:center;gap:5px;padding-left:6px}
.phone-back{left:25px;top:296px;width:139px;height:20px;border-radius:10px;background:var(--navy);display:flex;align-items:center;gap:6px;padding-left:3px}
.phone-back .num{font-size:16px;font-weight:800;color:#fff}
.phone-back .icon-circle{background:#fff}
.address{left:25px;top:324px;display:flex;gap:5px;font-size:7px;font-weight:600;line-height:9px}
.agent{top:275px;width:56px;text-align:center}
.agent.broker{left:176px}
.agent.realtor{left:240px}
.portrait{width:44px;height:44px;margin:0 auto;border-radius:50%;background:radial-gradient(circle,#c7c9cb,#a9abad);border:2px solid #9fd3e3}
.agent .role{margin-top:3px;font-size:7px;font-weight:600;border-bottom:1px solid var(--teal);padding-bottom:1px}
.agent .name{font-size:8px;font-weight:700;color:var(--teal-dark);margin-top:2px;white-space:nowrap}
.brand-back{left:322px;top:44px;width:96px;text-align:center;color:var(--navy);font-size:12px;font-weight:700;line-height:1;white-space:nowrap}
.brand-back .dot{display:block;width:10px;height:10px;background:var(--teal);border-radius:50%;margin:0 auto 5px}
.stamp{left:424px;top:28px;width:54px;height:54px;border:1px solid #888}
.addr-line{left:335px;width:144px;height:1px;background:#999}
</style>
</head>
<body>
<div class="side-label front">Postcard Front</div>
<div class="side-label back">Postcard Back</div>

<section class="card front">
  <svg class="front-art" width="504" height="364" viewBox="0 0 504 364">
    <defs>
      <linearGradient id="photoTone" x1="0" y1="0" x2="1" y2="1">
        <stop offset="0" stop-color="var(--photo-a)"/>
        <stop offset="1" stop-color="var(--photo-b)"/>
      </linearGradient>
    </defs>
    <polygon points="182,50 504,50 504,252 302,252" fill="url(#photoTone)" role="img" aria-label="Photo of a smiling agent shaking hands with a couple at a kitchen table"/>
    <polygon points="328,252 504,252 504,258 331,258" fill="var(--teal)"/>
    <polygon points="0,246 218,246 288,364 0,364" fill="var(--navy)"/>
    <polygon points="262,312 504,290 504,364 288,364" fill="var(--teal)"/>
    <polygon points="470,364 504,300 504,364" fill="var(--navy-deep)"/>
  </svg>
  <div class="abs brand-front"><span class="dot"></span>crestway homes<small>AS LOW AS 2% COMMISSION</small></div>
  <div class="abs sell-box"></div>
  <div class="abs sell-word">SELL</div>
  <div class="abs home-band">YOUR HOME</div>
  <div class="abs low-as">FOR AS LOW AS</div>
  <div class="abs pct">2%</div>
  <div class="abs commission">COMMISSION</div>
  <p class="abs note one">We list for 2%. If a buyer contacts us about your property, we handle the whole transaction for 2%.</p>
  <p class="abs note two">The Buyer's agent commission is 2%. If an agent from another company sells your property, the total commission is 4%.</p>
  <div class="abs cta-name">Crestway Homes Myrtle Beach</div>
  <div class="abs phone-pill">
    <span class="icon-circle"><svg width="9" height="9" viewBox="0 0 24 24"><path fill="#fff" d="M6.6 10.8a15 15 0 0 0 6.6 6.6l2.2-2.2c.3-.3.7-.4 1-.2 1.1.4 2.3.6 3.6.6.6 0 1 .4 1 1V20c0 .6-.4 1-1 1C10.6 21 3 13.4 3 4c0-.6.4-1 1-1h3.5c.6 0 1 .4 1 1 0 1.3.2 2.5.6 3.6.1.3 0 .7-.2 1z"/></svg></span>
    <span class="num">843-555-0172</span>
  </div>
  <div class="abs slogan">We sell Myrtle Beach</div>
</section>

<section class="card back">
  <div class="abs save">SAVE THOUSANDS</div>
  <div class="abs fees-band">IN COMMISSION FEES</div>
  <div class="abs local">We have local knowledge with over <b>1,000 closings in Horry County</b></div>
  <div class="abs not-a">We are not a</div>
  <div class="abs discount">discount Broker</div>
  <div class="abs service-grid">
    <div class="service">We meet with you for In-home consultation</div>
    <div class="service">We list in the MLS</div>
    <div class="service">Professional photography, lockbox, and yard sign.</div>
    <div class="service">Internet marketing, Dwellora, Quillhaven.com and 80 websites.</div>
    <div class="service">Handle all paperwork, offers and negotiations.</div>
    <div class="service">Manage inspections and closing.</div>
  </div>
  <div class="abs whats">What's your</div>
  <div class="abs worth">home worth?</div>
  <div class="abs email-band">RECEIVE A NO OBLIGATION EMAIL</div>
  <div class="abs research">We research comparable sales to find the best price for your home.</div>
  <div class="abs send">Send us an email with the property address.</div>
  <div class="abs email-bar">
    <svg width="8" height="6" viewBox="0 0 16 12"><rect x="1" y="1" width="14" height="10" fill="none" stroke="#fff" stroke-width="1.5"/><path d="M1 1l7 6 7-6" fill="none" stroke="#fff" stroke-width="1.5"/></svg>
    dana@crestwayhomesmb.com
  </div>
  <div class="abs phone-back">
    <span class="icon-circle"><svg width="9" height="9" viewBox="0 0 24 24"><path fill="var(--navy)" d="M6.6 10.8a15 15 0 0 0 6.6 6.6l2.2-2.2c.3-.3.7-.4 1-.2 1.1.4 2.3.6 3.6.6.6 0 1 .4 1 1V20c0 .6-.4 1-1 1C10.6 21 3 13.4 3 4c0-.6.4-1 1-1h3.5c.6 0 1 .4 1 1 0 1.3.2 2.5.6 3.6.1.3 0 .7-.2 1z"/></svg></span>
    <span class="num">843-555-0172</span>
  </div>
  <div class="abs address">
    <svg width="6" height="8" viewBox="0 0 12 16"><path d="M6 0a6 6 0 0 0-6 6c0 4.5 6 10 6 10s6-5.5 6-10a6 6 0 0 0-6-6zm0 8.5A2.5 2.5 0 1 1 6 3.5a2.5 2.5 0 0 1 0 5z" fill="var(--teal)"/></svg>
    <span>480 Harborline Dr<br>Myrtle Beach, SC 29577</span>
  </div>
  <div class="abs agent broker">
    <div class="portrait" role="img" aria-label="Portrait of the broker"></div>
    <div class="role">BROKER</div>
    <div class="name">Dana Whitford</div>
  </div>
  <div class="abs agent realtor">
    <div class="portrait" role="img" aria-label="Portrait of the realtor"></div>
    <div class="role">REALTOR</div>
    <div class="name">Carla Benson</div>
  </div>
  <div class="abs brand-back"><span class="dot"></span>crestway homes</div>
  <div class="abs stamp"></div>
  <div class="abs addr-line" style="top:186px"></div>
  <div class="abs addr-line" style="top:219px"></div>
  <div class="abs addr-line" style="top:253px"></div>
</section>
</body>
</html>
```